San Francisco Leading Consulting firm - 47Nova Web Design Project

•Create a Web Design
•Uncoded webpage layout design
•2 Pages Design - Homepage + Interior Page

Task Description
Hello, we're looking for a re-design our current website www.47nova-example.com

we have a sample mockup design @

http://47nova.civicpane-example.org/

This shows the layout that we like and also a sample of 6 pictures that would change based on where you mouse over..

6 pictures HOME design needs to be included.

SMART
THOUGHTFUL
FLEXIBLE
CREATIVE SERVICES
TECHNICAL SERVICES
PARTNERS

sites we like:

http://www.brelmoradvisory-example.com/Home.cfm?id=Home
http://www.pixelquarry-example.com/index.html

Our company can be best described as: 100+ employees, cutting-edge, depandable, innovative, strong, smart.

Our Primary focus is: IT Consulting Services and Creative Design services

47Nova LLC is a consulting firm providing creative design, business and technology solutions to both private and public interests.

Established in 1996, 47Nova is a San Francisco based company providing specialists for a range of business needs including:

Creative Design Services
•Print
•Logo Design
•Website Design
•Illustration

and

Business and Technology solutions

•Application Software and Web Development
•Business Process Re-Design (BPR)
•Business/Systems Analysis and Requirement Documentation
•Mentoring and Training
•Network/Hardware Installation Services
•System Design and Architecture
•Vendor Management
•Teamvault Architecture and Implementation

our sample mockup site:

Reason: Due to holiday season, we're not available to work with designers and finilize our design.  

Thank you very much for submitting your design.

We appreciate your time and creativity.   Since, our office is currently closed for holidays, we will be reviewing it in details next week and will make our decision as soon as possible.

It would be great if you could submit any of your changes by Wed next week, so it would be part of our reviews. 

Please see updated wireframe under attachments:  we have some minor updates to our wireframe that we would like you to update your designs, if possible.  

We also encorouge you not to use our standard wireframe and come up with more unique designs.   Everything would be considered when we review your design.

 

Target Market(s)

Creative services and professional services clients, including government agencies

Industry/Entity Type

Business

Requirements
Must have
• Clean, professional look, easy navigation

```html
<!DOCTYPE html>
<html lang="en">
<head>
<meta charset="utf-8">
<title>47Nova — Home</title>
<link rel="stylesheet" href="https://fonts.googleapis.com/css2?family=Cinzel:wght@400;700&family=Arimo:wght@400;700&family=Montserrat:wght@500&display=swap">
<style>
:root{
  --page:#ffffff;
  --band-light:#e4e5e7;
  --band-mid:#b9bbbf;
  --band-dark:#a3a5aa;
  --nav-grey:#dcdcdc;
  --brand-blue:#1e62a6;
  --nav-text:#2e5a8c;
  --nav-active:#8e1b8e;
  --logo-ink:#2b2d31;
  --heading:#3a3a3a;
  --body:#8a8a8a;
  --body-strong:#4a4a4a;
  --soft-heading:#a0a0a0;
  --rule:#9a9a9a;
  --accent-list:#5a9ad6;
}
*{margin:0;padding:0;box-sizing:border-box}
html,body{width:1200px;height:793px;overflow:hidden;background:var(--page)}
body{position:relative;font-family:"Cinzel",serif;color:var(--body)}
.abs{position:absolute}
.photo{position:absolute}

.hero-ghost{left:287px;top:0;width:284px;height:80px;background:linear-gradient(180deg,#c9d7e8,#dfe7f1);opacity:.7}
.frame-ghost{left:6px;top:22px;width:997px;height:93px;border:1px solid #eef0f3}

.masthead{left:116px;top:79px;width:934px;height:173px;
  background:linear-gradient(180deg,var(--band-light) 0%,var(--band-mid) 55%,var(--band-dark) 100%)}
.masthead svg{position:absolute;left:0;top:0}
.brand{left:130px;top:140px;display:flex;align-items:center;gap:18px}
.brand-dot{width:40px;height:40px;border-radius:50%;background:var(--brand-blue)}
.brand-name{font-family:"Montserrat",sans-serif;font-weight:500;font-size:50px;letter-spacing:4px;color:var(--logo-ink)}
.hero-bridge{left:560px;top:69px;width:455px;height:128px;
  background:linear-gradient(180deg,#5e7ea6 0%,#8a95a8 45%,#b07a4a 75%,#3a3a48 100%)}

.nav-shadow{left:222px;top:268px;width:708px;height:44px;background:var(--brand-blue)}
.nav{left:201px;top:252px;width:717px;height:48px;background:var(--nav-grey);
  display:flex;align-items:center;padding-left:18px;padding-top:2px;
  font-family:"Arimo",sans-serif;font-weight:700;font-size:12px;color:var(--nav-text)}
.nav a{color:inherit;text-decoration:none}
.nav a.active{color:var(--nav-active)}
.nav .sep{margin:0 11px;color:var(--nav-text)}

.side-shade{left:235px;top:300px;width:51px;height:367px;background:linear-gradient(90deg,#fff,#bfbfbf)}
.content{left:286px;top:300px;width:600px;height:367px;background:#fff}
.divider-v{left:683px;top:326px;width:1px;height:339px;background:var(--rule)}
.rule{height:1px;background:var(--rule)}

.welcome-title{left:328px;top:340px;font-size:13px;font-weight:700;letter-spacing:1.5px;color:var(--heading)}
.welcome-photo{left:287px;top:376px;width:106px;height:72px;border-radius:4px;
  background:linear-gradient(180deg,#d9dde2,#6b6e74 60%,#2e3034)}
.welcome-copy{left:413px;top:374px;width:262px;font-size:8.5px;line-height:13.6px;letter-spacing:.6px;color:var(--body)}
.welcome-copy b{color:var(--body-strong)}
.more{font-size:9px;letter-spacing:.6px;color:var(--body)}

.small{font-size:7px;letter-spacing:.6px;color:var(--body-strong)}
.tiny-copy{font-size:6.5px;line-height:10px;letter-spacing:.5px;color:var(--body)}
.tiny-copy b{color:var(--body-strong)}
.section-title{font-size:13px;letter-spacing:1.8px;color:var(--soft-heading)}

.aside-photo{left:684px;top:368px;width:173px;height:48px;
  background:linear-gradient(180deg,#5f7ea4,#9a8f8a 55%,#a26a3d 80%,#2f3140)}

.blue-tab{width:39px;height:17px;background:var(--brand-blue)}
.link-item{left:742px;font-size:6.5px;line-height:11px;letter-spacing:.5px;color:var(--body-strong);border-bottom:1px solid var(--rule);padding-bottom:1px}
.foot-link{font-size:6.5px;letter-spacing:.5px;color:var(--body-strong);border-bottom:1px solid var(--rule);padding:0 1px 2px}

.values{left:896px;top:358px;font-family:"Arimo",sans-serif;font-size:11.5px;line-height:16.7px;letter-spacing:2px;color:var(--accent-list)}
.values li{list-style:none}

.footer-band{left:203px;top:700px;width:783px;height:52px;
  background:linear-gradient(180deg,#d0d1d4,#b5b7bb 60%,#c7c8cb)}
.copyright{left:462px;top:767px;font-size:8px;letter-spacing:.8px;color:#9a9a9a}
</style>
</head>
<body>
  <div class="abs hero-ghost" role="img" aria-label="Faded photo of a circuit board"></div>
  <div class="abs frame-ghost"></div>

  <header>
    <div class="abs masthead">
      <svg width="934" height="173" viewBox="0 0 934 173" aria-hidden="true">
        <path d="M0 110 C 220 160, 520 70, 934 95 L934 173 L0 173 Z" fill="#d6d7da" opacity=".55"/>
        <path d="M180 173 C 420 120, 700 120, 934 150" stroke="#eeeeef" stroke-width="3" fill="none" opacity=".8"/>
      </svg>
    </div>
    <div class="abs brand">
      <span class="brand-dot"></span>
      <span class="brand-name">47NOVA</span>
    </div>
    <div class="photo hero-bridge" role="img" aria-label="Photo of a suspension bridge and the San Francisco skyline at dusk"></div>

    <div class="abs nav-shadow"></div>
    <nav class="abs nav">
      <a class="active" href="#">Home</a><span class="sep">I</span>
      <a href="#">Thought Leadership</a><span class="sep">I</span>
      <a href="#">News</a><span class="sep">I</span>
      <a href="#">Industries</a><span class="sep">I</span>
      <a href="#">Solutions for...</a><span class="sep">I</span>
      <a href="#">Strategic Technologies</a>
    </nav>
  </header>

  <main>
    <div class="abs side-shade"></div>
    <div class="abs content"></div>
    <div class="abs divider-v"></div>

    <h1 class="abs welcome-title">Welcome To 47Nova</h1>
    <div class="photo welcome-photo" role="img" aria-label="Group photo of the consulting team"></div>
    <p class="abs welcome-copy"><b>This is were all began</b>, major solution to hi-tech probles Some are clients include major industrie brands, and leaders of industrie. Since 1998 weve been on the fore front of latest developments...</p>
    <span class="abs more" style="left:413px;top:444px">More</span>
    <div class="abs rule" style="left:319px;top:472px;width:340px"></div>

    <p class="abs small" style="left:697px;top:347px;font-size:6.5px">Located in San Francisco</p>
    <div class="photo aside-photo" role="img" aria-label="Photo of the bridge and city lights"></div>
    <p class="abs tiny-copy" style="left:697px;top:427px;color:var(--body-strong)">Serving clients across the Bay.<br>Visit our downtown studio &nbsp; more</p>
    <div class="abs rule" style="left:699px;top:472px;width:163px"></div>

    <h2 class="abs section-title" style="left:371px;top:490px">Solutions</h2>
    <div class="photo" style="left:301px;top:488px;width:59px;height:78px;background:linear-gradient(180deg,#7fb2e0,#3d5f86)" role="img" aria-label="Photo of a glass office tower"></div>
    <p class="abs tiny-copy" style="left:372px;top:521px;width:130px"><b>Another paragr</b>aph discribing what we do best an how are service is second to none in are feild</p>
    <div class="photo" style="left:300px;top:580px;width:62px;height:54px;background:linear-gradient(180deg,#5a5c60,#2c2e33)" role="img" aria-label="Photo of a consultant at a workstation"></div>
    <p class="abs tiny-copy" style="left:372px;top:588px;width:130px"><b>Another paragr</b>aph discribing what we do an how are service is second to none in ar</p>
    <span class="abs foot-link" style="left:335px;top:650px">links overview</span>

    <h2 class="abs section-title" style="left:508px;top:490px">Solutions</h2>
    <div class="photo" style="left:500px;top:508px;width:78px;height:77px;background:linear-gradient(180deg,#f2eeea,#c9ad97)" role="img" aria-label="Photo of a support agent with a headset"></div>
    <p class="abs tiny-copy" style="left:569px;top:521px;width:112px">Another paragraph discribing what we do best an how are service is second to none in are feild call today</p>
    <span class="abs foot-link" style="left:520px;top:650px">links overview</span>

    <h2 class="abs section-title" style="left:697px;top:490px">Solutions</h2>
    <div class="abs blue-tab" style="left:695px;top:528px"></div>
    <p class="abs link-item" style="top:524px">Some links today<br>view case studies</p>
    <div class="abs blue-tab" style="left:695px;top:567px"></div>
    <p class="abs link-item" style="top:565px">Some links today<br>view case studies</p>
    <div class="abs blue-tab" style="left:695px;top:610px"></div>
    <p class="abs link-item" style="top:608px">Some links today<br>view case studies</p>
    <span class="abs foot-link" style="left:710px;top:650px">links more</span>

    <ul class="abs values">
      <li>SMART</li>
      <li>THOUGHTFUL</li>
      <li>FLEXIBLE</li>
      <li>CREATIVE SERVICES</li>
      <li>TECHNICAL SERVICES</li>
    </ul>
  </main>

  <footer>
    <div class="abs footer-band"></div>
    <p class="abs copyright">©2010, 47Nova, LLC All rights reserved</p>
  </footer>
</body>
</html>
```